Corvatel Website Graphic design

we want a replacement of existing designs in our existing website.. we want you to suggest and create a better graphical designs which suits our service with good representation explaining our process and services
Website Url: https://corvatelq.example
Basic Requirements -
1. Flat architecture
2. A good color palette
3. Icons to support the Content
4. Consistent Images in alignment with the Business
5. Use white space to let the Content breathe

Target Market(s)

Manufacturers & E-Commerce Distributors

Industry/Entity Type

Data Service

Colors

Designer to choose colors to be used in the design.

Requirements
Must have
• Creativity and originality
Nice to have
• Try to keep it Simple

```html
<!DOCTYPE html>
<html lang="en">
<head>
<meta charset="utf-8">
<title>Corvatel Solutions</title>
<link href="https://fonts.googleapis.com/css2?family=Poppins:wght@300;400;500;600;700&display=swap" rel="stylesheet">
<style>
:root{
  --navy:#2e2f6e;
  --navy-deep:#22234f;
  --orange:#e0692a;
  --purple:#7a3fe0;
  --purple-deep:#5528c0;
  --lavender:#eeeef8;
  --charcoal:#2f2f2f;
  --ink:#1c1c24;
  --muted:#6b6b78;
  --line:#cfd0dc;
  --white:#ffffff;
}
*{box-sizing:border-box;margin:0;padding:0}
html,body{width:1200px;height:5111px;overflow:hidden}
body{font-family:'Poppins',sans-serif;color:var(--ink);background:var(--white)}
.page{position:relative;width:1200px;height:5111px;overflow:hidden}
.abs{position:absolute}
section{position:absolute;left:0;width:1200px}

/* hero */
.hero{top:0;height:597px;background:linear-gradient(160deg,#3a3d7e 0%,#2b2c66 45%,#454a8c 100%)}
.brand{position:absolute;left:175px;top:24px;display:flex;align-items:center;gap:10px;color:var(--white);font-weight:500;font-size:22px;line-height:1}
.brand-dot{width:26px;height:26px;border-radius:50%;background:var(--orange)}
.nav{position:absolute;right:172px;top:30px;display:flex;gap:26px;font-size:12px;color:var(--white);font-weight:500}
.hero-title{position:absolute;left:170px;top:212px;color:var(--white);line-height:1.15}
.hero-title .light{font-weight:300;font-size:40px;display:block}
.hero-title .bold{font-weight:700;font-size:44px;display:block}
.hero-text{position:absolute;left:172px;top:335px;width:335px;color:#e6e7f5;font-size:11px;line-height:1.55}
.hero-visual{position:absolute;left:625px;top:180px;width:380px;height:265px;border-radius:130px;background:linear-gradient(135deg,#6a6fa8,#3b3e7c 60%,#5a5f98)}

/* headings */
.eyebrow{font-size:11px;font-weight:500;letter-spacing:.5px;color:var(--orange);text-transform:uppercase}
.rule{width:50px;height:2px;background:var(--orange);margin-top:8px}
.h2{font-weight:700;font-size:24px;text-transform:uppercase;color:var(--ink)}
.centered{position:absolute;left:0;width:1200px;text-align:center}

/* services */
.services{top:597px;height:503px;background:var(--white)}
.svc-card{position:absolute;top:289px;width:203px;height:139px;background:var(--white);box-shadow:0 6px 22px rgba(40,40,90,.13);text-align:center;font-size:13px;line-height:1.35;padding-top:56px}
.svc-icon{position:absolute;left:50%;top:-34px;margin-left:-33px;width:66px;height:66px;border-radius:50%;background:var(--white);box-shadow:0 3px 12px rgba(40,40,90,.18);display:flex;align-items:center;justify-content:center}

/* industries */
.industries{top:1100px;height:615px;background:var(--lavender)}
.tile{position:absolute;width:205px;height:174px;display:flex;align-items:center;justify-content:center;text-align:center;color:var(--white);font-size:14px;line-height:1.35;text-transform:uppercase}

/* about */
.about{top:1715px;height:456px;background:var(--charcoal)}
.about-photo{position:absolute;left:170px;top:78px;width:429px;height:297px;background:linear-gradient(180deg,#c7ccd6,#6b6f7e 60%,#3a3b46)}
.about-copy{position:absolute;left:656px;top:100px;width:340px;color:var(--white)}
.about-copy h3{font-size:24px;font-weight:700;margin-top:24px}
.about-copy h4{font-size:14px;font-weight:400;margin-top:6px}
.about-copy p{font-size:11px;line-height:1.35;margin-top:8px;color:#e2e2e2}
.btn{display:inline-block;background:var(--orange);color:var(--white);font-size:10px;font-weight:600;text-transform:uppercase}
.about-copy .btn{margin-top:26px;width:109px;height:27px;line-height:27px;text-align:center}

/* ai services */
.ai{top:2171px;height:1186px;background:var(--white)}
.ai-band{position:absolute;left:0;top:0;width:1200px;height:249px;background:linear-gradient(120deg,var(--purple) 0%,#6a34d6 60%,var(--purple-deep) 100%)}
.ai-title{top:92px;color:var(--white);font-size:24px;font-weight:600}
.ai-card{position:absolute;left:170px;top:153px;width:859px;height:692px;background:var(--white);box-shadow:0 8px 28px rgba(40,40,90,.12)}
.src{position:absolute;height:48px;border:1px solid var(--line);display:flex;align-items:center;justify-content:center;font-size:14px;color:#333}
.svc-row{position:absolute;left:58px;display:flex;align-items:center;gap:22px;font-size:14px;line-height:1.2}
.stage{position:absolute;left:318px;width:240px;height:58px;border:1px solid var(--line);display:flex;align-items:center;justify-content:center;text-align:center;font-size:11px;font-weight:600;line-height:1.35}
.feature{position:absolute;top:877px;height:256px;color:var(--white);text-align:center;padding:40px 36px 0}
.feature h4{font-size:15px;font-weight:600;text-transform:uppercase;margin-bottom:16px}
.feature p{font-size:11px;line-height:1.35}
.f-purple{background:linear-gradient(160deg,#8a4ff0,#5d2dc7)}
.f-orange{background:var(--orange)}

/* blogs */
.blogs{top:3357px;height:649px;background:var(--white)}
.blogs .eyebrow{color:var(--ink)}
.blog-head{position:absolute;left:170px;top:105px;width:420px;font-size:25px;font-weight:700;line-height:1.35;text-transform:uppercase}
.blog-sub{position:absolute;left:170px;top:252px;font-size:14px;text-transform:uppercase}
.impact{position:absolute;width:134px;height:126px;background:var(--white);box-shadow:0 4px 18px rgba(40,40,90,.1);text-align:center;font-size:11px;line-height:1.3;color:#6a6a8c;padding-top:72px}
.impact svg{position:absolute;left:50%;top:18px;margin-left:-21px}
.blog-photo{position:absolute;left:636px;top:48px;width:393px;height:547px;background:linear-gradient(170deg,#d8d9dd,#8f939c 55%,#4c4f58)}

/* contact */
.contact{top:4006px;height:436px;background:var(--white)}
.contact h3{position:absolute;left:170px;top:80px;font-size:24px;font-weight:700;text-transform:uppercase}
.contact .intro{position:absolute;left:172px;top:128px;width:460px;font-size:11px;line-height:1.3;color:var(--muted)}
.field{position:absolute;background:#eef0f6;border:1px solid #dde0ea;font-size:10px;color:#8a8a9a;padding:10px 14px}
.contact .btn{position:absolute;left:172px;top:321px;width:106px;height:30px;line-height:30px;text-align:center}
.map{position:absolute;left:690px;top:69px;width:339px;height:290px;background:linear-gradient(135deg,#eef0ea,#e2e6dc)}

/* sample */
.sample{top:4442px;height:669px;background:var(--white)}
.sample-band{position:absolute;left:0;top:133px;width:1200px;height:536px;background:linear-gradient(120deg,var(--purple) 0%,#6833d6 55%,var(--purple-deep) 100%)}
.sample-card{position:absolute;left:170px;top:26px;width:857px;height:267px;background:var(--white);box-shadow:0 10px 30px rgba(30,20,90,.18);text-align:center}
.sample-card h3{margin-top:78px;font-size:25px;font-weight:600}
.sample-card p{margin-top:6px;font-size:12px}
.sample-card .field{top:156px;height:34px}
.sample-card .btn{position:absolute;left:582px;top:156px;width:117px;height:34px;line-height:34px;text-align:center;font-size:12px}
.foot-brand{position:absolute;left:0;width:1200px;top:357px;display:flex;justify-content:center;align-items:center;gap:14px;color:var(--white);font-size:32px;font-weight:500}
.foot-brand .brand-dot{width:34px;height:34px;background:var(--white)}
.social{position:absolute;left:0;width:1200px;top:478px;display:flex;justify-content:center;gap:44px}
.social span{width:18px;height:18px;border-radius:50%;background:var(--white)}
.foot-contact{position:absolute;top:545px;display:flex;align-items:center;gap:12px;color:var(--white);font-size:12px;line-height:1.3}
</style>
</head>
<body>
<div class="page">

  <section class="hero">
    <div class="brand"><span class="brand-dot"></span>Corvatel Solutions</div>
    <nav class="nav"><span>Home</span><span>About</span><span>Services</span><span>Solution</span><span>Contact</span></nav>
    <h1 class="hero-title"><span class="light">CORVATEL</span><span class="bold">SOLUTIONS</span></h1>
    <p class="hero-text">Get your business critical data seamlessly integrated into your systems. Standardize and enrich data to provide better visibility into sourcing and procurement. Solutions to Extract, Analyse, Clean up, Validate and Enrich your data</p>
    <div class="hero-visual" role="img" aria-label="Photograph of a team working at an office desk"></div>
  </section>

  <section class="services">
    <div class="centered eyebrow" style="top:74px">Our Services<div class="rule" style="margin:10px auto 0"></div></div>
    <div class="centered h2" style="top:130px">Better Data Better Decisions Better ROI</div>
    <p class="centered" style="top:175px;font-size:14px;line-height:1.3">Our value added services help companies realize the full potential<br>of ERP and e-Commerce implementations.</p>

    <div class="svc-card" style="left:169px">
      <div class="svc-icon"><svg width="40" height="40" viewBox="0 0 40 40"><circle cx="20" cy="20" r="17" fill="var(--orange)"/><circle cx="20" cy="20" r="11" fill="var(--navy)"/><rect x="14" y="19" width="3" height="7" fill="#fff"/><rect x="19" y="15" width="3" height="11" fill="#fff"/><rect x="24" y="17" width="3" height="9" fill="#fff"/></svg></div>
      Master Data<br>Management
    </div>
    <div class="svc-card" style="left:387px">
      <div class="svc-icon"><svg width="40" height="40" viewBox="0 0 40 40"><rect x="6" y="10" width="22" height="18" rx="2" fill="var(--orange)"/><rect x="10" y="14" width="14" height="2" fill="#fff"/><rect x="10" y="19" width="10" height="2" fill="#fff"/><circle cx="28" cy="24" r="7" fill="none" stroke="var(--navy)" stroke-width="3"/><line x1="33" y1="29" x2="37" y2="33" stroke="var(--navy)" stroke-width="3"/></svg></div>
      E-commerce<br>Data Configuration
    </div>
    <div class="svc-card" style="left:605px">
      <div class="svc-icon"><svg width="40" height="40" viewBox="0 0 40 40"><path d="M8 22a12 12 0 0 1 24 0" fill="none" stroke="var(--navy)" stroke-width="3"/><rect x="5" y="20" width="7" height="11" rx="3" fill="var(--orange)"/><rect x="28" y="20" width="7" height="11" rx="3" fill="var(--orange)"/><circle cx="20" cy="22" r="4" fill="var(--navy)"/></svg></div>
      Support<br>Services
    </div>
    <div class="svc-card" style="left:823px">
      <div class="svc-icon"><svg width="40" height="40" viewBox="0 0 40 40"><circle cx="20" cy="20" r="14" fill="var(--navy)"/><circle cx="20" cy="20" r="16" fill="none" stroke="var(--navy)" stroke-width="3" stroke-dasharray="4 4"/><circle cx="20" cy="20" r="6" fill="var(--orange)"/></svg></div>
      AI based<br>Data Services
    </div>
  </section>

  <section class="industries">
    <div class="centered h2" style="top:62px">Data Drives Business</div>
    <p class="centered" style="top:104px;font-size:14px">Unlock the maximum value from your Data</p>
    <div class="tile" style="left:170px;top:159px;background:linear-gradient(135deg,#3b5a86,#2c3f60)" role="img" aria-label="Aerospace engine photograph">Aerospace</div>
    <div class="tile" style="left:389px;top:159px;background:linear-gradient(135deg,#5b5d4e,#3c3e37)" role="img" aria-label="Defense personnel photograph">Defense</div>
    <div class="tile" style="left:607px;top:159px;background:linear-gradient(135deg,#5a6670,#3a434b)" role="img" aria-label="Oil and gas plant photograph">Oil &amp; Gas</div>
    <div class="tile" style="left:823px;top:159px;background:linear-gradient(135deg,#6a6a72,#46464e)" role="img" aria-label="Industrial manufacturing photograph">Industrial<br>Manufacturing</div>
    <div class="tile" style="left:170px;top:348px;background:linear-gradient(135deg,#2f6a8e,#23485f)" role="img" aria-label="Electronic circuit board photograph">Electronic<br>Components</div>
    <div class="tile" style="left:389px;top:348px;background:linear-gradient(135deg,#7a5a3a,#4d3826)" role="img" aria-label="Food and beverage photograph">Food &amp;<br>Beverage</div>
    <div class="tile" style="left:607px;top:348px;background:linear-gradient(135deg,#7d8894,#525c66)" role="img" aria-label="Laboratory photograph">Life<br>Sciences</div>
    <div class="tile" style="left:823px;top:348px;background:linear-gradient(135deg,#9a6a5a,#6a7a4a)" role="img" aria-label="Coloured yarn spools photograph">Textile</div>
  </section>

  <section class="about">
    <div class="about-photo" role="img" aria-label="Photograph of the company leadership team"></div>
    <div class="about-copy">
      <div class="eyebrow" style="color:var(--white)">About Us</div>
      <div class="rule"></div>
      <h3>OUR COMPANY</h3>
      <h4>CORVATEL SOLUTIONS</h4>
      <p>Corvatel Solutions specializes in extracting business centric information from large, complex and disparate sources to realize full potential of Enterprise and E-Commerce implementations</p>
      <span class="btn">Read More</span>
    </div>
  </section>

  <section class="ai">
    <div class="ai-band"></div>
    <div class="centered ai-title">AI BASED DATA SERVICES</div>
    <div class="ai-card">
      <div class="src" style="left:46px;top:60px;width:177px">ERP</div>
      <div class="src" style="left:236px;top:60px;width:173px">3rd Party Sources</div>
      <div class="src" style="left:423px;top:60px;width:172px">Streaming Data</div>
      <div class="src" style="left:609px;top:60px;width:177px">Catalogs</div>

      <div class="svc-row" style="top:178px"><svg width="44" height="44" viewBox="0 0 44 44" fill="none" stroke="var(--orange)" stroke-width="2"><rect x="4" y="10" width="16" height="16"/><rect x="24" y="4" width="16" height="16"/><rect x="14" y="28" width="16" height="12"/><line x1="20" y1="18" x2="24" y2="12"/></svg><span>Integration<br>Services</span></div>
      <div class="svc-row" style="top:270px"><svg width="44" height="44" viewBox="0 0 44 44" fill="none" stroke="var(--orange)" stroke-width="2"><circle cx="22" cy="22" r="16"/><circle cx="22" cy="22" r="6" stroke="var(--navy)"/><line x1="22" y1="2" x2="22" y2="10"/><line x1="22" y1="34" x2="22" y2="42"/></svg><span>Orchestration<br>Services</span></div>
      <div class="svc-row" style="top:361px"><svg width="44" height="44" viewBox="0 0 44 44" fill="none" stroke="var(--orange)" stroke-width="2"><circle cx="12" cy="14" r="8"/><rect x="24" y="22" width="16" height="16" stroke="var(--navy)"/><path d="M12 24v10h10"/></svg><span>Transformation<br>Services</span></div>
      <div class="svc-row" style="top:450px"><svg width="44" height="44" viewBox="0 0 44 44" fill="none" stroke="var(--orange)" stroke-width="2"><rect x="4" y="6" width="28" height="20"/><circle cx="32" cy="30" r="6" stroke="var(--navy)"/><path d="M22 42c0-6 4-8 10-8s10 2 10 8" stroke="var(--navy)"/></svg><span>Advisory<br>Services</span></div>

      <div class="stage" style="top:173px">DATA STAGING</div>
      <div class="stage" style="top:266px">ML | BIG DATA PRE-<br>PROCESSING | ENRICHMENT</div>
      <div class="stage" style="top:359px">NLP | AI | CONTEXT<br>POST-PROCESSING</div>
      <div class="stage" style="top:450px">BUSINESS AUTOMATION</div>

      <svg class="abs" style="left:689px;top:145px" width="100" height="400" viewBox="0 0 100 400">
        <rect x="25" y="0" width="50" height="60" rx="25" fill="var(--orange)"/>
        <rect x="25" y="40" width="50" height="100" fill="var(--navy)"/>
        <rect x="25" y="130" width="50" height="110" fill="var(--orange)"/>
        <rect x="25" y="230" width="50" height="110" fill="var(--navy)"/>
        <polygon points="0,338 100,338 50,400" fill="var(--navy)"/>
        <circle cx="50" cy="69" r="46" fill="var(--orange)"/><circle cx="50" cy="69" r="38" fill="#fff"/>
        <circle cx="50" cy="176" r="46" fill="var(--navy)"/><circle cx="50" cy="176" r="38" fill="#fff"/>
        <circle cx="50" cy="287" r="46" fill="var(--orange)"/><circle cx="50" cy="287" r="38" fill="#fff"/>
        <text x="50" y="73" font-family="Poppins,sans-serif" font-size="11" text-anchor="middle" fill="#222">ACQUIRE</text>
        <text x="50" y="180" font-family="Poppins,sans-serif" font-size="11" text-anchor="middle" fill="#222">PROCESS</text>
        <text x="50" y="291" font-family="Poppins,sans-serif" font-size="11" text-anchor="middle" fill="#222">TRANSFORM</text>
      </svg>

      <div class="src" style="left:46px;top:571px;width:177px">EAM</div>
      <div class="src" style="left:236px;top:571px;width:173px">PLM</div>
      <div class="src" style="left:423px;top:571px;width:172px">E-Com</div>
      <div class="src" style="left:609px;top:571px;width:177px">Social Platforms</div>
    </div>

    <div class="feature f-purple" style="left:170px;width:274px"><h4>Acquire Data</h4><p>Integrate data from desperate sources such as ERP, Affiliate &amp; 3rd Party Feeds, OEM Catalogs, Distributors, Suppliers, Streaming Data without disrupting your production swim lane</p></div>
    <div class="feature f-orange" style="left:462px;width:276px"><h4>Making Sense of Data</h4><p>Our machine learning engines detect patterns in the data and make sense out of it to render the data actionable in real time for managing assets, monitoring business operations and potentially identify new transformational opportunities</p></div>
    <div class="feature f-purple" style="left:755px;width:274px"><h4>Business Automation</h4><p>Driven by real time actionable insights automate business processes for delivering results. Our mature business automation capabilities can deliver scalable business automation delivered on an industry leading business automation platform</p></div>
  </section>

  <section class="blogs">
    <div class="abs eyebrow" style="left:170px;top:54px">Blogs<div class="rule"></div></div>
    <h3 class="blog-head">Operating with a bad data is more expensive than the cost of improving data quality</h3>
    <p class="blog-sub">5 Major impacts of bad MRO data</p>

    <div class="impact" style="left:170px;top:302px"><svg width="42" height="42" viewBox="0 0 42 42" fill="none" stroke="var(--orange)" stroke-width="2"><rect x="8" y="4" width="22" height="30"/><line x1="12" y1="12" x2="26" y2="12"/><line x1="12" y1="18" x2="26" y2="18"/><rect x="24" y="26" width="14" height="12" stroke="var(--navy)"/></svg>Unreasonable<br>high inventory</div>
    <div class="impact" style="left:317px;top:302px"><svg width="42" height="42" viewBox="0 0 42 42" fill="none" stroke="var(--orange)" stroke-width="2"><circle cx="21" cy="16" r="10"/><text x="21" y="20" font-size="11" text-anchor="middle" fill="var(--orange)" stroke="none">$</text><path d="M6 38h30l-4-8H10z" stroke="var(--navy)"/></svg>Excessive<br>procurement<br>cost</div>
    <div class="impact" style="left:462px;top:302px"><svg width="42" height="42" viewBox="0 0 42 42" fill="none" stroke="var(--orange)" stroke-width="2"><rect x="4" y="6" width="34" height="24"/><line x1="14" y1="36" x2="28" y2="36" stroke="var(--navy)"/><circle cx="21" cy="18" r="6" stroke="var(--navy)"/></svg>Unplanned<br>maintenance<br>downtime</div>
    <div class="impact" style="left:170px;top:443px"><svg width="42" height="42" viewBox="0 0 42 42" fill="none" stroke="var(--orange)" stroke-width="2"><rect x="4" y="8" width="34" height="26"/><line x1="12" y1="16" x2="12" y2="28" stroke="var(--navy)"/><line x1="20" y1="14" x2="20" y2="28" stroke="var(--navy)"/><line x1="28" y1="18" x2="28" y2="28" stroke="var(--navy)"/></svg>Design failures</div>
    <div class="impact" style="left:317px;top:443px"><svg width="42" height="42" viewBox="0 0 42 42" fill="none" stroke="var(--orange)" stroke-width="2"><rect x="6" y="14" width="24" height="22"/><line x1="6" y1="22" x2="30" y2="22"/><path d="M32 4a6 6 0 0 1 6 6c0 5-6 10-6 10s-6-5-6-10a6 6 0 0 1 6-6z" stroke="var(--navy)"/></svg>Inappropriateness<br>of storage<br>location</div>

    <div class="blog-photo" role="img" aria-label="Photograph of a presenter beside a desk with laptops"></div>
  </section>

  <section class="contact">
    <h3>Please get in touch</h3>
    <p class="intro">We'd love to hear from you. If you've got questions, feedback or ideas you would like to share, For anything more specific, please use form below</p>
    <div class="field" style="left:172px;top:178px;width:149px;height:32px">First Name</div>
    <div class="field" style="left:333px;top:178px;width:149px;height:32px">Last Name</div>
    <div class="field" style="left:494px;top:178px;width:148px;height:32px">Email</div>
    <div class="field" style="left:172px;top:222px;width:470px;height:79px">Message</div>
    <span class="btn">Send Now</span>
    <div class="map" role="img" aria-label="Street map showing the office location">
      <svg class="abs" style="left:140px;top:96px" width="24" height="32" viewBox="0 0 24 32"><path d="M12 0a12 12 0 0 1 12 12c0 9-12 20-12 20S0 21 0 12A12 12 0 0 1 12 0z" fill="#e2372b"/><circle cx="12" cy="12" r="4" fill="#fff"/></svg>
    </div>
  </section>

  <section class="sample">
    <div class="sample-band"></div>
    <div class="sample-card">
      <h3>Request For Sample Data</h3>
      <p>Claim your Free Data Cleansing and Enrichment offer here !</p>
      <div class="field" style="left:127px;width:221px;text-align:left">Full Name</div>
      <div class="field" style="left:356px;width:220px;text-align:left">Your Email Id</div>
      <span class="btn">Send</span>
    </div>
    <div class="foot-brand"><span class="brand-dot"></span>Corvatel Solutions</div>
    <div class="social" aria-label="Social links"><span></span><span></span><span></span></div>
    <div class="foot-contact" style="left:258px"><svg width="16" height="16" viewBox="0 0 16 16"><path d="M3 1l3 1 1 4-2 1a9 9 0 0 0 4 4l1-2 4 1 1 3-2 2C7 15 1 9 1 3z" fill="#fff"/></svg>USA: +1-555-010-0142</div>
    <div class="foot-contact" style="left:531px"><svg width="18" height="13" viewBox="0 0 18 13"><rect width="18" height="13" fill="#fff"/><path d="M0 0l9 7 9-7" fill="none" stroke="var(--purple)" stroke-width="1.5"/></svg>info@corvatelq.example</div>
    <div class="foot-contact" style="left:750px"><svg width="14" height="18" viewBox="0 0 14 18"><path d="M7 0a7 7 0 0 1 7 7c0 5-7 11-7 11S0 12 0 7a7 7 0 0 1 7-7z" fill="#fff"/><circle cx="7" cy="7" r="2.5" fill="var(--purple)"/></svg><span>4120 Larkfield Way, Alder Park,<br>CA 90000, USA</span></div>
  </section>

</div>
</body>
</html>
```